Website design for Interior Designer

We want a modern website design for an Interior designer. The website should include completed and undergoing projects, CV, services, news, contact and media gallery pages.

Target Market(s)

People or companies who want to design their properties.

Industry/Entity Type

Interior

Number of Pages Required

5+ page

Requirements
Must have
• Related to interior design.
• Portrait of the designer.
• Her CV.
• Current and completed projects.
• Colours as the attached document.
• Pages mentioned in the description
Nice to have
• Like these websites – but don't copy them😊
• www.plovanstudio.co.za
• www.brightwellfixes.co.za
• www.tkstudioltd.com
• others-
• www.haraldbeuk.de/en
• www.emfairley.co.uk/
• Hope that gives you a starting point.

```html
<!DOCTYPE html>
<html lang="en">
<head>
<meta charset="utf-8">
<title>Mira Castell — Senior Interior Designer</title>
<link href="https://fonts.googleapis.com/css2?family=Mulish:wght@400;600;700;800&display=swap" rel="stylesheet">
<style>
  :root {
    --ink: #333333;
    --muted: #a3a3a3;
    --white: #ffffff;
    --tile: #f2f2f2;
    --accent-cyan: #19f5d9;
    --accent-yellow: #f7fb00;
    --client-purple: #4b1f86;
    --client-blue: #1d6fa5;
    --client-orange: #f24a0a;
    --photo-light: #e9e6e1;
    --photo-wood: #9c7a5b;
    --photo-dark: #5e4a39;
  }
  * { box-sizing: border-box; margin: 0; padding: 0; }
  html, body { width: 1200px; height: 1000px; overflow: hidden; background: var(--white); }
  body { font-family: "Mulish", Arial, sans-serif; color: var(--ink); position: relative; }

  .hero { position: absolute; left: 0; top: 0; width: 1200px; height: 600px; box-shadow: 0 14px 24px rgba(0,0,0,0.06); }
  .sidebar { position: absolute; left: 0; top: 0; width: 305px; height: 600px; background: var(--white); }
  .brand-mark { position: absolute; left: 70px; top: 48px; width: 86px; height: 90px; background: var(--accent-yellow); }
  .brand-name { position: absolute; left: 71px; top: 170px; font-size: 31px; font-weight: 700; letter-spacing: 0.5px; line-height: 1.1; }
  .brand-role { position: absolute; left: 71px; top: 208px; font-size: 13px; letter-spacing: 0.2px; color: #555; }

  .main-nav { position: absolute; left: 72px; top: 286px; list-style: none; }
  .main-nav li { font-size: 18px; font-weight: 700; color: var(--muted); line-height: 23px; margin-bottom: 12px; letter-spacing: 0.3px; }
  .main-nav li.is-active { color: var(--ink); position: relative; }
  .main-nav li.is-active::before { content: ""; position: absolute; left: -72px; top: 5px; width: 59px; height: 14px; background: var(--accent-cyan); }

  .hero-photo { position: absolute; left: 305px; top: 0; width: 895px; height: 600px;
    background: linear-gradient(180deg, var(--photo-light) 0%, #d9d6d1 45%, var(--photo-wood) 62%, #b08a66 80%, var(--photo-dark) 100%); }

  .about-card { position: absolute; left: 775px; top: 136px; width: 321px; height: 357px; background: var(--white); padding: 26px 36px 0 36px; }
  .about-card h2 { font-size: 29px; font-weight: 700; letter-spacing: 0.5px; line-height: 1; margin-bottom: 6px; }
  .about-card .lead { font-size: 16px; line-height: 19.5px; margin-bottom: 14px; }
  .about-card .body { font-size: 12.5px; line-height: 15px; }

  .clients { position: absolute; left: 0; top: 600px; width: 1200px; height: 400px; text-align: center; }
  .clients h2 { position: absolute; left: 0; right: 0; top: 50px; font-size: 29px; font-weight: 700; letter-spacing: 0.5px; }
  .clients .intro { position: absolute; left: 0; right: 0; top: 114px; font-size: 16px; }

  .client-grid { position: absolute; left: 157px; top: 200px; width: 895px; display: grid; grid-template-columns: repeat(5, 179px); grid-auto-rows: 188px; }
  .client { display: flex; align-items: center; justify-content: center; gap: 10px; font-size: 20px; font-weight: 600; }
  .client.shade { background: var(--tile); }
  .client .dot { width: 40px; height: 40px; flex: none; }
  .client--lumora { color: var(--client-purple); }
  .client--lumora .dot { background: var(--client-purple); }
  .client--halden { color: var(--client-blue); }
  .client--orrin { color: var(--ink); }
  .client--orrin .dot { background: var(--client-orange); }
</style>
</head>
<body>
  <header class="hero">
    <aside class="sidebar">
      <div class="brand-mark"></div>
      <h1 class="brand-name">MIRA CASTELL</h1>
      <p class="brand-role">SENIOR INTERIOR DESIGNER</p>
      <ul class="main-nav">
        <li>PAST AND<br>CURRENT PROJECTS</li>
        <li class="is-active">ABOUT ME</li>
        <li>NEWS</li>
        <li>MEDIA</li>
        <li>CONTACT</li>
      </ul>
    </aside>
    <div class="hero-photo" role="img" aria-label="Photo of a designer's desk with a computer showing charts, plant, keyboard, notebook, phone and rolled plans"></div>
    <section class="about-card">
      <h2>ABOUT ME</h2>
      <p class="lead">Here you can talk about yourself, what makes you unique and remarquable. You could use a beautiful photo of your office, your working environment, or really anything that you feel reflects your personality as a designer.</p>
      <p class="body">vero eos et accusamus et iusto odio dignissimos ducimus qui blanditiis praesentium voluptatum deleniti atque corrupti quos dolores et quas molestias excepturi sint occaecati cupiditate non provident, similique</p>
    </section>
  </header>

  <section class="clients">
    <h2>CLIENTS</h2>
    <p class="intro">Lorem ipsum dolor amet, corvus raptum caseum.</p>
    <div class="client-grid">
      <div class="client shade client--lumora"><span class="dot"></span>Lumora</div>
      <div class="client client--halden">Halden &amp; Co</div>
      <div class="client shade client--orrin"><span class="dot"></span>Orrin Works</div>
      <div class="client client--lumora"><span class="dot"></span>Lumora</div>
      <div class="client shade client--halden">Halden &amp; Co</div>
      <div class="client"></div>
      <div class="client shade"></div>
      <div class="client"></div>
      <div class="client shade"></div>
      <div class="client"></div>
    </div>
  </section>
</body>
</html>
```